Letterhead for New Orthopaedic Surgery Practice

My husband and I are starting our own practice named RB Spine & Vitality Center. We would like to create a nice simple but high class letterhead that doesn't use too much solid color ink when printing. I like the colors dark blue, gold, yellow. Open to other suggestions. We will need to list him and I both on the top of the letterhead. Here is the important information:
Lucinda Perrow, M.D. - Hand and Upper Extremity Surgery
Abena Quist, M.D. - Hip & Knee Replacement/General Orthopaedic Surgery
Location: 18735 North Harlow Pkwy
Maple Harbor, FL 33418
Phone: 954-218-4650
Fax: 954-582-1346
Email: info@myrbspine.com

The only thing is that the phone and fax numbers will change once we get into our space. I just want to get the design started. I am including several documents which are my previous practice letterhead, my current procedure room letterhead, and our new Logo. The other letterheads are just for examples but please think outside of the box! We would love to see some great designs.

Colors
0054AA
0677BA
7BADD7
CADEEF
E8F1F8
0094D4
00A9DD
6FCCEA
C7EBF8
E9F6FB

Requirements
Must have
• class, elegance, luxury

```html
<!DOCTYPE html>
<html lang="en">
<head>
<meta charset="utf-8">
<title>RB Spine &amp; Vitality Center — Letterhead</title>
<link href="https://fonts.googleapis.com/css2?family=Lato:wght@400;700&family=PT+Sans:wght@400&display=swap" rel="stylesheet">
<style>
  :root {
    --navy: #1b2a52;
    --gold: #c9a24a;
    --rule: #e9dcc0;
    --ink: #2b2b2b;
    --paper: #ffffff;
    --backdrop: #bdbdbd;
  }
  * { box-sizing: border-box; margin: 0; padding: 0; }
  html, body { width: 1200px; height: 878px; overflow: hidden; }
  body {
    background: var(--backdrop);
    font-family: "PT Sans", sans-serif;
    color: var(--ink);
  }
  .sheet {
    position: absolute;
    left: 303px; top: 19px;
    width: 594px; height: 840px;
    background: var(--paper);
    box-shadow: 0 6px 18px rgba(0,0,0,.18);
    overflow: hidden;
  }
  .masthead { position: absolute; inset: 0 0 auto 0; height: 170px; }
  .masthead-band { position: absolute; left: 0; top: 0; }
  .physicians {
    position: absolute; left: 34px; top: 82px;
    list-style: none; font-family: "Lato", sans-serif;
  }
  .physicians li { position: relative; padding-left: 12px; margin-bottom: 4px; }
  .physicians li::before {
    content: ""; position: absolute; left: 0; top: 6px;
    width: 4px; height: 4px; border-radius: 50%; background: var(--gold);
  }
  .physician-name { display: block; color: #fff; font-size: 12px; line-height: 15px; }
  .physician-specialty { display: block; color: var(--gold); font-size: 8px; line-height: 10px; }
  .contact {
    position: absolute; right: 26px; top: 34px;
    text-align: right; font-family: "Lato", sans-serif; font-style: normal;
    color: #fff; font-size: 9.5px; line-height: 13px;
  }
  .contact-line { display: flex; justify-content: flex-end; align-items: center; gap: 5px; }
  .contact-line svg { width: 9px; height: 9px; fill: var(--gold); }
  .address { margin-bottom: 3px; padding-right: 14px; }
  .brand-seal {
    position: absolute; left: 241px; top: 44px;
    width: 112px; height: 112px; border-radius: 50%;
    background: var(--paper);
    display: flex; align-items: center; justify-content: center;
    text-align: center;
  }
  .brand-name {
    font-family: "Lato", sans-serif; font-weight: 700;
    color: var(--navy); font-size: 12.5px; line-height: 15px;
    width: 86px; letter-spacing: .3px;
  }
  .letter-body {
    position: absolute; left: 58px; top: 318px; width: 470px;
    font-size: 10.5px; line-height: 13.5px;
  }
  .salutation { font-size: 12px; margin-bottom: 26px; }
  .letter-body p { margin-bottom: 14px; }
  .closing { position: absolute; left: 58px; top: 640px; font-size: 10.5px; }
  .signature {
    display: block; width: 80px; height: 34px; margin: 8px 0 4px 14px;
    background: linear-gradient(90deg, #d9d9d9, #bcbcbc);
    border-radius: 4px;
  }
  .signer { padding-left: 30px; }
  .footer-rule {
    position: absolute; right: 28px; bottom: 46px;
    width: 330px; height: 1px; background: var(--rule);
  }
</style>
</head>
<body>
  <main class="sheet">
    <header class="masthead">
      <svg class="masthead-band" width="594" height="170" viewBox="0 0 594 170" aria-hidden="true">
        <path d="M0 62 H297 V28 H594 V112 H297 V150 H0 Z" fill="var(--navy)"/>
      </svg>

      <ul class="physicians">
        <li>
          <span class="physician-name">Lucinda Perrow, M.D.</span>
          <span class="physician-specialty">Hand and Upper Extremity Surgery</span>
        </li>
        <li>
          <span class="physician-name">Abena Quist, M.D.</span>
          <span class="physician-specialty">Hip &amp; Knee Replacement/General Orthopaedic Surgery</span>
        </li>
      </ul>

      <div class="brand-seal">
        <span class="brand-name">RB Spine &amp; Vitality Center</span>
      </div>

      <address class="contact">
        <div class="address">18735 North Harlow Pkwy<br>Maple Harbor, FL 33418</div>
        <div class="contact-line">954-218-4650
          <svg viewBox="0 0 10 10"><path d="M2 1 L4 1 L4.6 3 L3.4 4 Q4.5 6 6 6.6 L7 5.4 L9 6 L9 8 Q8.5 9 7.5 9 Q1 8 1 2.5 Q1 1.5 2 1 Z"/></svg>
        </div>
        <div class="contact-line">954-582-1346
          <svg viewBox="0 0 10 10"><rect x="2.5" y="1" width="5" height="3"/><rect x="1" y="4" width="8" height="4.5" rx="1"/></svg>
        </div>
        <div class="contact-line">info@myrbspine.com
          <svg viewBox="0 0 10 10"><path d="M1 2.5 H9 V8 H1 Z M1 2.5 L5 5.5 L9 2.5" stroke="#1b2a52" stroke-width=".6"/></svg>
        </div>
      </address>
    </header>

    <section class="letter-body">
      <p class="salutation">Dear Sir</p>
      <p>Lorem Ipsum is simply dummy text of the printing and typesetting industry. Lorem Ipsum has been the industry's standard dummy text ever since the 1500s, when an unknown printer took a galley of type and scrambled it to make a type specimen book. It has survived not only five centuries, but also the leap into electronic typesetting, remaining essentially unchanged.</p>
      <p>It was popularised in the 1960s with the release of Typeline sheets containing Lorem Ipsum passages, and more recently with desktop publishing software like Pageform Studio including versions of Lorem Ipsum.</p>
      <p>Lorem Ipsum is simply dummy text of the printing and typesetting industry. Lorem Ipsum has been the industry's standard dummy text ever since the 1500s, when an unknown printer took a galley of type and scrambled it to make a type specimen book.</p>
      <p>It has survived not only five centuries, but also the leap into electronic typesetting, remaining essentially unchanged. It was popularised in the 1960s with the release of Typeline sheets containing Lorem Ipsum passages, and more recently with desktop publishing software like Pageform Studio including versions of Lorem Ipsum.</p>
    </section>

    <footer class="closing">
      <p>Sincerly</p>
      <span class="signature" role="img" aria-label="Handwritten signature"></span>
      <p class="signer">Lucinda Perrow, M.D.</p>
    </footer>

    <div class="footer-rule"></div>
  </main>
</body>
</html>
```